Harbin Motors LLC

Car Dealer Customer Service
Address: 2847 Calloway Avenue, Fairhaven, ND 58099
web: www.harbinmotorsco.example
email: harbinmotorsco@mailbox.example
Phone: (555) 555-0147
Phone: (555) 555-0183

```html
<!DOCTYPE html>
<html lang="en">
<head>
<meta charset="utf-8">
<title>Harbin Motors LLC – Business Card</title>
<link href="https://fonts.googleapis.com/css2?family=Montserrat:wght@500;600;700;800&display=swap" rel="stylesheet">
<style>
  :root{
    --backdrop:#2a2a2c;
    --card:#1b1b1c;
    --card-edge:#232325;
    --brand-blue:#1f7fbf;
    --gold:#d9a43a;
    --gold-light:#f0c868;
    --gold-dark:#a8771f;
  }
  *{margin:0;padding:0;box-sizing:border-box}
  html,body{width:1200px;height:800px;overflow:hidden}
  body{
    background:var(--backdrop);
    font-family:'Montserrat',sans-serif;
    display:flex;flex-direction:column;align-items:center;justify-content:center;gap:44px;
  }
  .card{
    position:relative;
    width:588px;height:336px;
    background:radial-gradient(ellipse at 40% 40%,var(--card-edge),var(--card) 70%);
    border-right:3px solid var(--gold);
    border-bottom:3px solid var(--gold);
    box-shadow:0 18px 40px rgba(0,0,0,.55);
  }
  /* front */
  .card-front{display:flex;align-items:center;justify-content:center}
  .front-brand{display:flex;flex-direction:column;align-items:center;gap:18px}
  .brand-dot{width:26px;height:26px;border-radius:50%;background:var(--gold)}
  .brand-name{
    color:var(--brand-blue);font-weight:800;font-size:40px;letter-spacing:1px;text-transform:uppercase;white-space:nowrap;
  }
  /* back */
  .card-back{display:flex;align-items:center;padding:0 30px 0 40px}
  .back-brand{width:200px;display:flex;flex-direction:column;align-items:center;gap:12px}
  .back-brand .brand-dot{width:18px;height:18px}
  .back-brand .brand-name{font-size:20px;letter-spacing:.5px}
  .divider{width:2px;height:150px;background:linear-gradient(var(--gold-light),var(--gold-dark));margin:0 24px 0 20px}
  .contact{flex:1}
  .tagline{color:var(--brand-blue);font-weight:800;font-size:14.5px;text-transform:uppercase;margin-bottom:8px;letter-spacing:.2px}
  .address{color:var(--gold);font-weight:600;font-size:14px;line-height:1.35;margin-bottom:6px}
  .contact-list{list-style:none}
  .contact-list li{display:flex;align-items:center;gap:9px;color:var(--gold);font-weight:600;font-size:14px;line-height:1.55}
  .contact-list svg{width:12px;height:12px;flex:none;fill:var(--brand-blue)}
</style>
</head>
<body>
  <section class="card card-front" aria-label="Card front">
    <div class="front-brand">
      <span class="brand-dot"></span>
      <span class="brand-name">Harbin Motors</span>
    </div>
  </section>

  <section class="card card-back" aria-label="Card back">
    <div class="back-brand">
      <span class="brand-dot"></span>
      <span class="brand-name">Harbin Motors</span>
    </div>
    <div class="divider"></div>
    <div class="contact">
      <p class="tagline">Car Dealer Customer Service</p>
      <p class="address">2847 Calloway Avenue, Fairhaven,<br>ND 58099</p>
      <ul class="contact-list">
        <li><svg viewBox="0 0 24 24"><path d="M6.6 10.8a15 15 0 0 0 6.6 6.6l2.2-2.2a1 1 0 0 1 1-.25 11.4 11.4 0 0 0 3.6.57 1 1 0 0 1 1 1V20a1 1 0 0 1-1 1A17 17 0 0 1 3 4a1 1 0 0 1 1-1h3.5a1 1 0 0 1 1 1c0 1.25.2 2.45.57 3.57a1 1 0 0 1-.25 1z"/></svg>(555) 555-0147</li>
        <li><svg viewBox="0 0 24 24"><path d="M6.6 10.8a15 15 0 0 0 6.6 6.6l2.2-2.2a1 1 0 0 1 1-.25 11.4 11.4 0 0 0 3.6.57 1 1 0 0 1 1 1V20a1 1 0 0 1-1 1A17 17 0 0 1 3 4a1 1 0 0 1 1-1h3.5a1 1 0 0 1 1 1c0 1.25.2 2.45.57 3.57a1 1 0 0 1-.25 1z"/></svg>(555) 555-0183</li>
        <li><svg viewBox="0 0 24 24"><path d="M2 5h20v14H2zm2 2v.5l8 5 8-5V7l-8 5z"/></svg>harbinmotorsco@mailbox.example</li>
        <li><svg viewBox="0 0 24 24"><path d="M12 2a10 10 0 1 0 0 20 10 10 0 0 0 0-20zm6.9 9h-3a15 15 0 0 0-1.3-5.6A8 8 0 0 1 18.9 11zM12 4c.9 1.2 1.8 3.6 1.9 7h-3.8c.1-3.4 1-5.8 1.9-7zM9.4 5.4A15 15 0 0 0 8.1 11h-3a8 8 0 0 1 4.3-5.6zM5.1 13h3a15 15 0 0 0 1.3 5.6A8 8 0 0 1 5.1 13zM12 20c-.9-1.2-1.8-3.6-1.9-7h3.8c-.1 3.4-1 5.8-1.9 7zm2.6-1.4a15 15 0 0 0 1.3-5.6h3a8 8 0 0 1-4.3 5.6z"/></svg>www.harbinmotorsco.example</li>
      </ul>
    </div>
  </section>
</body>
</html>
```